Business Card for Air Cargo Brokerage

Hi Artvoyant -

Please see the images attached. I need a business card with a similar image and format but modernized. Business card should be portrait and have room for a QR code.

Thanks

```html
<!DOCTYPE html>
<html lang="en">
<head>
<meta charset="utf-8">
<title>Skyward Freight – Business Card</title>
<link rel="stylesheet" href="https://fonts.googleapis.com/css2?family=Open+Sans:wght@400;600;700&display=swap">
<style>
  :root {
    --page-bg: #f2f0ed;
    --front-dark: #0f0f0f;
    --front-mid: #2b2b2b;
    --front-light: #5a5a5a;
    --back-light: #f1f1f1;
    --back-mid: #e3e3e3;
    --ink: #111111;
    --paper: #ffffff;
    --rule: #d0d0d0;
    --frame: #8a8a8a;
  }
  * { box-sizing: border-box; margin: 0; padding: 0; }
  html, body {
    width: 1200px;
    height: 777px;
    overflow: hidden;
    background: var(--page-bg);
    font-family: "Open Sans", Arial, sans-serif;
  }
  .canvas {
    position: relative;
    width: 1200px;
    height: 777px;
  }
  .card {
    position: absolute;
    top: 48px;
    width: 360px;
    height: 680px;
    overflow: hidden;
    box-shadow: 0 6px 18px rgba(0,0,0,0.22);
  }
  .card--front { left: 200px; color: var(--paper); }
  .card--back  { left: 640px; color: var(--ink); }

  .card__pattern {
    position: absolute;
    inset: 0;
  }
  .card--front .card__pattern {
    background: linear-gradient(180deg, var(--front-light) 0%, var(--front-mid) 35%, var(--front-dark) 70%, var(--front-mid) 100%);
  }
  .card--back .card__pattern {
    background: linear-gradient(180deg, var(--back-mid) 0%, var(--back-light) 55%, var(--back-mid) 100%);
  }

  .brand-dot {
    position: absolute;
    border-radius: 50%;
  }
  .card--front .brand-dot--main {
    width: 86px; height: 86px;
    left: 137px; top: 229px;
    background: var(--paper);
  }
  .card--front .brand-dot--corner {
    width: 40px; height: 40px;
    left: 310px; top: 567px;
    background: var(--paper);
  }
  .card--back .brand-dot--main {
    width: 80px; height: 80px;
    left: 140px; top: 42px;
    background: var(--ink);
  }

  .brand-name, .tagline, .person-name, .person-role, .contact-line {
    position: absolute;
    left: 0;
    width: 100%;
    text-align: center;
    white-space: nowrap;
  }
  .brand-name {
    font-weight: 700;
    font-size: 33px;
    line-height: 1;
    letter-spacing: -0.2px;
  }
  .tagline {
    font-weight: 400;
    font-size: 12.5px;
    letter-spacing: 0.3px;
  }
  .card--front .brand-name { top: 330px; }
  .card--front .tagline { top: 368px; }
  .card--back .brand-name { top: 135px; }
  .card--back .tagline { top: 172px; }

  .qr-frame {
    position: absolute;
    left: 70px;
    top: 208px;
    width: 249px;
    height: 245px;
    background: var(--paper);
    border: 1px solid var(--frame);
  }

  .person-name {
    top: 468px;
    font-weight: 700;
    font-size: 31px;
    line-height: 1;
  }
  .person-role {
    top: 503px;
    font-weight: 400;
    font-size: 16px;
    letter-spacing: 1px;
  }
  .divider {
    position: absolute;
    left: 100px;
    top: 532px;
    width: 190px;
    height: 1px;
    background: var(--rule);
  }
  .contact-icons {
    position: absolute;
    top: 548px;
    left: 0;
    width: 100%;
    display: flex;
    justify-content: center;
    gap: 40px;
  }
  .contact-icons svg { width: 22px; height: 22px; display: block; }
  .contact-line {
    font-size: 18px;
    font-weight: 400;
    line-height: 1;
  }
  .contact-line--phone { top: 580px; }
  .contact-line--email { top: 602px; }
  .contact-line--web   { top: 624px; }
</style>
</head>
<body>
<main class="canvas">

  <section class="card card--front">
    <div class="card__pattern" role="img" aria-label="Repeating embossed pattern of small aircraft silhouettes across a black card"></div>
    <span class="brand-dot brand-dot--main"></span>
    <h1 class="brand-name">Skyward Freight</h1>
    <p class="tagline">SOLUTIONS FOR GLOBAL AIR COMMERCE</p>
    <span class="brand-dot brand-dot--corner"></span>
  </section>

  <section class="card card--back">
    <div class="card__pattern" role="img" aria-label="Repeating embossed pattern of small aircraft silhouettes across a light grey card"></div>
    <span class="brand-dot brand-dot--main"></span>
    <h2 class="brand-name">Skyward Freight</h2>
    <p class="tagline">SOLUTIONS FOR GLOBAL AIR COMMERCE</p>

    <div class="qr-frame" aria-label="Space for QR code"></div>

    <p class="person-name">Daniel Morrow</p>
    <p class="person-role">MANAGING DIRECTOR</p>
    <span class="divider"></span>

    <div class="contact-icons">
      <svg viewBox="0 0 22 22" aria-label="Phone">
        <rect width="22" height="22" rx="2" fill="var(--ink)"/>
        <path d="M5 8 q6 -4 12 0 v2 h-3 v-1.5 q-3 -1 -6 0 V10 H5z" fill="var(--paper)"/>
        <rect x="6" y="11" width="10" height="6" rx="1" fill="var(--paper)"/>
        <circle cx="11" cy="14" r="1.6" fill="var(--ink)"/>
      </svg>
      <svg viewBox="0 0 22 22" aria-label="Email">
        <rect width="22" height="22" rx="2" fill="var(--ink)"/>
        <rect x="4" y="6" width="14" height="10" fill="var(--paper)"/>
        <path d="M4 6 L11 12 L18 6" fill="none" stroke="var(--ink)" stroke-width="1.3"/>
      </svg>
      <svg viewBox="0 0 22 22" aria-label="Location">
        <rect width="22" height="22" rx="2" fill="var(--ink)"/>
        <path d="M11 4 a5 5 0 0 1 5 5 c0 4 -5 9 -5 9 s-5 -5 -5 -9 a5 5 0 0 1 5 -5z" fill="var(--paper)"/>
        <circle cx="11" cy="9" r="2" fill="var(--ink)"/>
      </svg>
    </div>

    <p class="contact-line contact-line--phone">000 -555 204 781</p>
    <p class="contact-line contact-line--email">info@skywardfr.com</p>
    <p class="contact-line contact-line--web">www.skywardfr.com</p>
  </section>

</main>
</body>
</html>
```